Business Card Design Project

Use newly designed logo and tie into newly designed website
I need a new logo and website layout designed for my partner's business. This is a birthday present. His business is interior painting, wallpapering and design. He also has access to a wide variety of products including carpet, fabrics, furniture, wallpaper, tile, countertops, etc. I have attached some screen shots of his website for reference. He is a one man shop and has a stellar reputation with his customers. He is on-time, very tidy, excellent with animals, and always finishes on time and on budget. There are no restrictions on colors or fonts. The logo needs to work well with the website, business cards and printed materials. The website needs to flow content for device size so it looks just as good on a cell phone or tablet as it does on a desktop computer. Whatever the heck that's called!Thanks. I am looking forward to seeing everyone's ideas.
Target Market(s)
Consumers looking to improve the interior environment of their homes by updating wall paint or paper, flooring (either carpet, tile, or hardwoods), counter tops, window treatments, etc. Clients tend to be more upper middle class and have certain taste levels and expectations. New logo, website and business card should align to meet those levels.
Industry/Entity Type
Cell Phone
Look and feel

```html
<!DOCTYPE html>
<html lang="en">
<head>
<meta charset="utf-8">
<title>Verano Business Card</title>
<link rel="stylesheet" href="https://fonts.googleapis.com/css2?family=Crimson+Text:wght@400;700&display=swap">
<style>
  :root {
    --accent: #dc7845;
    --ink: #2b2b2b;
    --paper: #ffffff;
    --rule: #3a3a3a;
    --pattern-tone: #ececec;
  }
  html, body {
    margin: 0;
    padding: 0;
    width: 1200px;
    height: 1000px;
    overflow: hidden;
    background: var(--paper);
  }
  .canvas {
    position: relative;
    width: 1200px;
    height: 1000px;
    font-family: "Crimson Text", Georgia, serif;
    color: var(--ink);
  }
  .card {
    position: absolute;
    left: 437px;
    top: 232px;
    width: 326px;
    height: 536px;
    box-sizing: border-box;
    border: 10px solid var(--accent);
    background: var(--paper);
    overflow: hidden;
  }
  .card__pattern {
    position: absolute;
    left: 118px;
    top: 160px;
    width: 190px;
    height: 360px;
    background: radial-gradient(ellipse at 75% 55%, var(--pattern-tone) 0%, rgba(236,236,236,0.5) 45%, rgba(255,255,255,0) 75%);
  }
  .brand {
    position: absolute;
    left: 0;
    right: 0;
    top: 88px;
    text-align: center;
    font-size: 26px;
    letter-spacing: 4px;
    font-weight: 400;
    color: var(--ink);
  }
  .person {
    position: absolute;
    left: 16px;
    top: 274px;
  }
  .person__name {
    margin: 0;
    font-size: 23px;
    font-weight: 700;
    line-height: 1;
    letter-spacing: 0.2px;
  }
  .person__first {
    border-bottom: 1.5px solid var(--rule);
    padding-bottom: 1px;
  }
  .person__role {
    margin: 3px 0 0;
    font-size: 17px;
    line-height: 1;
    color: var(--accent);
  }
  .contacts {
    position: absolute;
    left: 16px;
    top: 398px;
    margin: 0;
    padding: 0;
    list-style: none;
    font-size: 15.5px;
    line-height: 21.5px;
  }
  .contacts__item {
    display: flex;
    align-items: flex-start;
  }
  .contacts__icon {
    flex: none;
    width: 16px;
    height: 17px;
    margin: 2px 6px 0 0;
  }
  .contacts__text--ruled {
    border-bottom: 1px solid var(--rule);
    line-height: 20px;
  }
  .contacts__address {
    display: block;
  }
  .contacts__address-line1 {
    border-bottom: 1px solid var(--rule);
  }
</style>
</head>
<body>
<div class="canvas">
  <div class="card">
    <div class="card__pattern" role="img" aria-label="Faint outlined hexagon pattern in pale grey"></div>

    <div class="brand">VERANO</div>

    <div class="person">
      <h1 class="person__name"><span class="person__first">DANE</span> VERANO.</h1>
      <p class="person__role">manager</p>
    </div>

    <ul class="contacts">
      <li class="contacts__item">
        <svg class="contacts__icon" viewBox="0 0 16 17" aria-hidden="true">
          <polygon points="8,0 15.5,4.25 15.5,12.75 8,17 0.5,12.75 0.5,4.25" fill="var(--accent)"/>
          <path d="M3.5 7.5 Q8 4 12.5 7.5 L11.5 8.5 L10 7.8 L10 7 Q8 6.3 6 7 L6 7.8 L4.5 8.5 Z" fill="#fff"/>
          <rect x="5" y="8.6" width="6" height="3.4" rx="0.6" fill="#fff"/>
        </svg>
        <span class="contacts__text">(555) 214-0387</span>
      </li>
      <li class="contacts__item">
        <svg class="contacts__icon" viewBox="0 0 16 17" aria-hidden="true">
          <polygon points="8,0 15.5,4.25 15.5,12.75 8,17 0.5,12.75 0.5,4.25" fill="var(--accent)"/>
          <rect x="3.5" y="5.5" width="9" height="6" fill="#fff"/>
          <path d="M3.5 5.5 L8 9 L12.5 5.5" fill="none" stroke="var(--accent)" stroke-width="1"/>
        </svg>
        <span class="contacts__text contacts__text--ruled">dane@veranodesigns.com</span>
      </li>
      <li class="contacts__item">
        <svg class="contacts__icon" viewBox="0 0 16 17" aria-hidden="true">
          <polygon points="8,0 15.5,4.25 15.5,12.75 8,17 0.5,12.75 0.5,4.25" fill="var(--accent)"/>
          <circle cx="8" cy="8.5" r="4.3" fill="none" stroke="#fff" stroke-width="1"/>
          <ellipse cx="8" cy="8.5" rx="1.8" ry="4.3" fill="none" stroke="#fff" stroke-width="0.8"/>
          <line x1="3.7" y1="8.5" x2="12.3" y2="8.5" stroke="#fff" stroke-width="0.8"/>
        </svg>
        <span class="contacts__text contacts__text--ruled">www.veranodesigns.com</span>
      </li>
      <li class="contacts__item">
        <svg class="contacts__icon" viewBox="0 0 16 17" aria-hidden="true">
          <polygon points="8,0 15.5,4.25 15.5,12.75 8,17 0.5,12.75 0.5,4.25" fill="var(--accent)"/>
          <path d="M8 13 C6 10.5 5 9 5 7.3 A3 3 0 0 1 11 7.3 C11 9 10 10.5 8 13 Z" fill="#fff"/>
          <circle cx="8" cy="7.3" r="1.1" fill="var(--accent)"/>
        </svg>
        <span class="contacts__address">
          <span class="contacts__address-line1">4820 W Linden Ct. Fairview,</span><br>KS 66000
        </span>
      </li>
    </ul>
  </div>
</div>
</body>
</html>
```